Wheatless Table Co Web Design

We are looking for designs for a homepage for a gluten free, health food website.

We are looking for the site to be a shop, as well as a resource/information source for users. We will also look to incorporate recipes, blogs, forums and potentially some other useful information.

We want to ensure that the website is user-friendly, does not have a corporate feel, but is still classy.

We want to have high quality photographic images in the background, with text in the foreground - but these things will need to compliment each other well. e.g recipe of the week integrated onto the background photo and the 'shop' in the foreground.

We have seen a site that we quite like and although we like the design, we do not want to completely emulate this. However, it is a useful starting point for designers and perhaps some inspiration www.brambleharvestgrocer.example

We already have a logo - see attached - which will need to be fully integrated into the design.

We do want a colourful design, but mainly in terms of the images rather than the graphics.
Updates

Please note:

We are pleased with the designs to date, for the most part. We would like you all to note, however, that we are much preferring the lighter designs - ones that make the sites feel brighter - rather than those which are darker in appearance.

We would also like to see less space allocated to the main image, within the context of the site as a whole.

Thanks.

We have eliminated those which we feel are not what we are looking for. We are still keen to see some more designs and are still looking for something unique. There are some good things in all of the designs that we have not eliminated, however we still feel there is room for more inspiration.

Thanks.

Target Market(s)

Our audience are body conscience people looking for health food products. They are also those who are potentially looking for a new lifestyle/life cha

Industry/Entity Type

Health

Requirements
Must have
• Our logo - attached, can provide variations in due course.

Navigational features as per mock up attached.

Social network integration.

NB: we only need one (home) page for this.

```html
<!DOCTYPE html>
<html lang="en">
<head>
<meta charset="utf-8">
<title>Wheatless Table Co</title>
<link href="https://fonts.googleapis.com/css2?family=Open+Sans:wght@400;600&display=swap" rel="stylesheet">
<style>
:root{
  --bg:#dfe4ea;
  --ink:#333;
  --muted:#555;
  --dark:#3a3a3a;
  --red:#e3262b;
  --green:#3aa935;
  --green-light:#dff0d8;
  --blue:#3aaec9;
  --blue-light:#cfe9f1;
  --link:#1b8fb0;
  --footer:#1e1e1e;
  --footer-band:#151515;
  --line:#3c3c3c;
}
*{box-sizing:border-box;margin:0;padding:0}
html,body{width:1200px;height:1059px;overflow:hidden}
body{position:relative;font-family:"Open Sans",Arial,sans-serif;color:var(--ink);
  background:linear-gradient(180deg,#eef1f4 0,#d7dde4 300px,#e6eaee 560px,#eef0f2 800px);}
.abs{position:absolute}
.site-header{left:0;top:0;width:1200px;height:100px;background:linear-gradient(#fff,#eef0f2);border-top:8px solid #c9d3dd;box-shadow:0 2px 4px rgba(0,0,0,.12)}
.brand{left:140px;top:0;width:162px;height:140px;background:#fff;border-radius:0 0 81px 81px;box-shadow:0 2px 4px rgba(0,0,0,.15);display:flex;flex-direction:column;align-items:center;justify-content:center;gap:8px}
.brand-dot{width:34px;height:34px;border-radius:50%;background:#2a2a2a}
.brand-name{font-size:15px;font-weight:600;color:#2a2a2a;text-align:center;line-height:1.2;width:120px}
.basket{left:527px;top:17px;width:201px;height:30px;display:flex;font-size:12px}
.basket span{flex:1;border:1px solid var(--red);color:var(--red);display:flex;align-items:center;justify-content:center;background:#fff}
.basket b{width:88px;background:var(--red);color:#fff;font-weight:400;font-size:14px;display:flex;align-items:center;justify-content:center}
.btn-dark{top:16px;height:31px;background:#1f1f1f;color:#fff;font-size:15px;display:flex;align-items:center;justify-content:center;border:1px solid #000}
.search{left:907px;top:16px;width:188px;height:31px;border:1px solid var(--green);background:#fff;display:flex;align-items:center;font-size:11px;font-style:italic;color:var(--green);padding-left:12px}
.search i{position:absolute;right:0;top:0;width:36px;height:29px;background:var(--green);display:flex;align-items:center;justify-content:center}
.main-nav{left:670px;top:64px;width:420px;display:flex;justify-content:flex-end;font-size:14px;color:#444}
.main-nav a{color:inherit;text-decoration:none;padding:0 9px;border-left:1px solid #aaa;line-height:16px}
.main-nav a:first-child{border-left:0}
.welcome{left:378px;top:130px;width:659px;height:40px;background:#3b3b3b;color:#fff;font-size:17px;display:flex;align-items:center;justify-content:center;box-shadow:0 2px 3px rgba(0,0,0,.2)}
.panel{background:#fff;border:1px solid #d6d6d6;box-shadow:0 1px 3px rgba(0,0,0,.1)}
.panel-head{height:38px;color:#fff;font-size:20px;display:flex;align-items:center;padding-left:22px;position:relative}
.panel-head svg{position:absolute;right:8px;top:7px}
.head-dark{background:#3a3a3a;justify-content:center;padding:0}
.head-red{background:var(--red)}
.head-blue{background:var(--blue);justify-content:center;padding:0}
.body-text{font-size:12px;line-height:18px;color:var(--muted)}
.about{left:98px;top:202px;width:230px;height:152px}
.about .body-text{padding:12px 12px}
.side-btn{left:98px;width:230px;height:36px;color:#fff;font-size:20px;display:flex;align-items:center;padding-left:16px;border:2px solid #fff;box-shadow:0 1px 3px rgba(0,0,0,.15)}
.feature{left:344px;top:204px;width:467px;height:272px}
.photo-main{left:13px;top:52px;width:230px;height:150px;background:radial-gradient(circle at 50% 50%,#f0e6c8,#d15a55 55%,#3d2a22)}
.thumb{top:213px;width:72px;height:50px;border:3px solid #eee}
.feature-copy{left:258px;top:50px;width:206px}
.feature-copy h3{font-weight:400;font-size:18px;color:#333;margin-bottom:12px}
.feature-copy a,.posts a,.tags a{color:var(--link);text-decoration:none}
.full-recipe{left:258px;top:242px;width:222px;height:27px;background:#3a3a3a;color:#fff;font-size:14px;display:flex;align-items:center;padding-left:15px}
.full-recipe svg{position:absolute;right:10px;top:8px}
.posts{left:828px;top:204px;width:268px;height:276px}
.post-date{left:10px;top:50px;color:var(--link);font-size:26px;line-height:28px}
.post-date small{display:block;font-size:9px;line-height:10px}
.post-title{left:58px;top:68px;font-size:18px;color:#444}
.posts .body-text{left:10px;top:106px;width:252px;position:absolute}
.tags{left:10px;top:206px;width:250px;font-size:11px;display:flex;justify-content:space-between}
.tags b{font-weight:600}
.post-foot{left:0;top:240px;width:266px;height:36px;display:flex}
.post-foot span{width:84px;background:var(--blue-light);color:var(--link);font-size:15px;display:flex;align-items:center;justify-content:center}
.post-foot em{flex:1;font-style:normal;color:var(--link);font-size:15px;display:flex;align-items:center;justify-content:flex-end;padding-right:40px}
.corner{position:absolute;right:0;bottom:0}
.product{top:506px;width:187px;height:238px}
.product-head{height:36px;background:var(--green);color:#fff;font-size:18px;display:flex;align-items:center;justify-content:center}
.product-img{height:162px}
.product-foot{height:36px;display:flex;position:relative}
.price{width:84px;background:var(--green-light);color:var(--green);font-size:18px;display:flex;align-items:center;justify-content:center}
.add{flex:1;font-size:14px;color:#444;display:flex;align-items:center;padding-left:18px}
.site-footer{left:0;top:800px;width:1200px;height:259px;background:var(--footer)}
.footer-band{left:0;top:0;width:1200px;height:40px;background:var(--footer-band)}
.footer-col{top:12px;color:#ddd}
.footer-col h4{font-weight:600;font-size:16px;color:#fff;margin-bottom:18px}
.link-list{list-style:none;font-size:12px;color:#ddd;width:232px}
.link-list li{height:30px;line-height:30px;padding-left:17px;border-bottom:1px solid var(--line)}
.newsletter p{font-size:12px;line-height:20px;width:200px;color:#eee;margin-bottom:14px}
.news-field{display:flex;width:216px;height:38px}
.news-field span{flex:1;background:#fff;border:1px solid var(--green)}
.news-field b{width:38px;background:var(--green);display:flex;align-items:center;justify-content:center}
.contact{font-size:12px;line-height:20px;color:#ddd}
.contact .mail{color:var(--green)}
.social{display:flex;gap:5px;margin-top:10px}
.social span{width:29px;height:29px;border-radius:2px}
.copyright{left:0;top:220px;width:1200px;height:39px;border-top:1px solid #333;font-size:10px;color:#ccc;display:flex;align-items:center;padding-left:211px}
</style>
</head>
<body>

<header class="site-header abs"></header>
<div class="brand abs">
  <span class="brand-dot"></span>
  <span class="brand-name">Wheatless Table Co</span>
</div>

<div class="basket abs"><span>0 Item(s) in</span><b>Basket</b></div>
<div class="btn-dark abs" style="left:737px;width:78px">Login</div>
<div class="btn-dark abs" style="left:821px;width:78px">Register</div>
<div class="search abs">Product search.....
  <i><svg width="18" height="18" viewBox="0 0 18 18"><circle cx="7.5" cy="7.5" r="5.5" fill="none" stroke="#fff" stroke-width="2.2"/><path d="M11.5 11.5l5 5" stroke="#fff" stroke-width="2.6" stroke-linecap="round"/></svg></i>
</div>
<nav class="main-nav abs">
  <a>Shop</a><a>Our Story</a><a>Hints &amp; tips</a><a>Recipes</a><a>Blog</a><a>Contact</a>
</nav>

<svg class="abs" style="left:378px;top:118px" width="660" height="70" viewBox="0 0 660 70">
  <path d="M0 12L37 2V12Z" fill="#5a5a5a"/>
  <path d="M623 52H659L659 56L623 68Z" fill="#b01d22"/>
</svg>
<div class="welcome abs">Welcome to Wheatless Table Co&nbsp; - &nbsp;The one stop shop for everthing Gluten Free</div>

<section class="about panel abs">
  <div class="panel-head head-dark">Wheatless Table Co</div>
  <p class="body-text">Ut scelerisque diam. Donec pulvinar ultricies sem, vel dapibus eros Maecenas auctor.Ut scelerisque diam. Donec pulvinar ultricies sem, vel dapibus eros Maecenas auctor.</p>
</section>
<a class="side-btn abs" style="top:360px;background:var(--blue)">Latest Posts</a>
<a class="side-btn abs" style="top:402px;background:var(--green)">View all Recipes</a>
<a class="side-btn abs" style="top:444px;background:var(--red)">Go to the Shop</a>

<section class="feature panel abs">
  <div class="panel-head head-red">New York baked cheesecake
    <svg width="16" height="14" viewBox="0 0 16 14"><path d="M1 5v8h12v-4" fill="none" stroke="#fff" stroke-width="1.5"/><path d="M6 9c1-4 4-5 8-5M11 1l3 3-3 3" fill="none" stroke="#fff" stroke-width="1.5"/></svg>
  </div>
  <div class="photo-main abs" role="img" aria-label="Photo of a baked cheesecake topped with strawberries"></div>
  <div class="thumb abs" style="left:16px;background:linear-gradient(#5a3526,#2e1c15)" role="img" aria-label="Photo of a layered chocolate cake"></div>
  <div class="thumb abs" style="left:96px;background:linear-gradient(135deg,#f3d5d8,#c7e3e8)" role="img" aria-label="Photo of pastel sweets"></div>
  <div class="thumb abs" style="left:177px;background:linear-gradient(135deg,#d8b37a,#6a7fa0)" role="img" aria-label="Photo of blueberry muffins"></div>
  <div class="feature-copy abs">
    <h3>Ut scelerisque diam.</h3>
    <p class="body-text">Donec pulvinar ultricies sem, vel dapibus eros Maecenas auctor.Ut scelerisque diam. Donec pulvinar ultricies sem, vel dapibus eros Maecenas auctor.</p>
    <p class="body-text" style="margin-top:18px">Ut scelerisque diam. Donec pulvinar ultricies sem, vel dapibus <a>more...</a></p>
  </div>
  <div class="full-recipe abs">Full&nbsp; Recipe
    <svg width="10" height="10" viewBox="0 0 10 10"><circle cx="4" cy="4" r="3" fill="none" stroke="#fff" stroke-width="1.3"/><path d="M6.2 6.2l3 3" stroke="#fff" stroke-width="1.5"/></svg>
  </div>
</section>

<section class="posts panel abs">
  <div class="panel-head head-blue">Latest Posts
    <svg width="16" height="14" viewBox="0 0 16 14"><path d="M1 5v8h12v-4" fill="none" stroke="#fff" stroke-width="1.5"/><path d="M6 9c1-4 4-5 8-5M11 1l3 3-3 3" fill="none" stroke="#fff" stroke-width="1.5"/></svg>
  </div>
  <div class="post-date abs">04<small>Jan 11</small></div>
  <div class="post-title abs">Donec pulvinar ultricies</div>
  <p class="body-text">vel dapibus eros Maecenas auctor quam sit amet ante tristique sodales.vel dapibus eros Maecenas auctor quam sit amet ante.&nbsp; tristique sodales.vel dapibus eros Maecenas auctor quam sit amet ante tristique <a>more...</a></p>
  <div class="tags abs"><span>Tags: <a>Latest new, Gluten free</a></span><b>- Ada Pennick</b></div>
  <div class="post-foot abs"><span>Blog</span><em>View all posts</em>
    <svg class="corner" width="38" height="36" viewBox="0 0 38 36"><path d="M38 0V36H0Z" fill="var(--blue)"/><circle cx="26" cy="24" r="4" fill="none" stroke="#fff" stroke-width="1.4"/><path d="M29 27l3 3" stroke="#fff" stroke-width="1.6"/></svg>
  </div>
</section>

<article class="product panel abs" style="left:98px">
  <div class="product-head">Product Name</div>
  <div class="product-img" style="background:radial-gradient(circle,#f0a04a 0,#f7e5c8 45%,#fff 70%)" role="img" aria-label="Photo of a box of oatcakes"></div>
  <div class="product-foot"><span class="price">£ 0.50</span><span class="add">Add to</span>
    <svg class="corner" width="34" height="34" viewBox="0 0 34 34"><path d="M34 0V34H0Z" fill="var(--green)"/><path d="M24 22v8M20 26h8" stroke="#fff" stroke-width="1.6"/></svg></div>
</article>
<article class="product panel abs" style="left:303px">
  <div class="product-head">Product Name</div>
  <div class="product-img" style="background:radial-gradient(circle,#f6a21e,#d9661b 60%,#f1e7dc)" role="img" aria-label="Photo of a bag of pretzels"></div>
  <div class="product-foot"><span class="price">£ 2.50</span><span class="add">Add to</span>
    <svg class="corner" width="34" height="34" viewBox="0 0 34 34"><path d="M34 0V34H0Z" fill="var(--green)"/><path d="M24 22v8M20 26h8" stroke="#fff" stroke-width="1.6"/></svg></div>
</article>
<article class="product panel abs" style="left:508px">
  <div class="product-head">Product Name</div>
  <div class="product-img" style="background:linear-gradient(90deg,#b58a52,#e3cfa4 25%,#9c6a3a 50%,#e3cfa4 75%,#b58a52)" role="img" aria-label="Photo of two loaves of gluten free bread"></div>
  <div class="product-foot"><span class="price">£ 5.50</span><span class="add">Add to</span>
    <svg class="corner" width="34" height="34" viewBox="0 0 34 34"><path d="M34 0V34H0Z" fill="var(--green)"/><path d="M24 22v8M20 26h8" stroke="#fff" stroke-width="1.6"/></svg></div>
</article>
<article class="product panel abs" style="left:711px">
  <div class="product-head">Product Name</div>
  <div class="product-img" style="background:radial-gradient(circle at 50% 55%,#1f3b2a 0,#1f3b2a 30%,#f2c23a 55%,#c9402c 90%)" role="img" aria-label="Photo of a pack of gluten free pasta with tomatoes"></div>
  <div class="product-foot"><span class="price">£ 4.98</span><span class="add">Add to</span>
    <svg class="corner" width="34" height="34" viewBox="0 0 34 34"><path d="M34 0V34H0Z" fill="var(--green)"/><path d="M24 22v8M20 26h8" stroke="#fff" stroke-width="1.6"/></svg></div>
</article>
<article class="product panel abs" style="left:914px">
  <div class="product-head">Product Name</div>
  <div class="product-img" style="background:linear-gradient(90deg,#b58a52,#e3cfa4 25%,#9c6a3a 50%,#e3cfa4 75%,#b58a52)" role="img" aria-label="Photo of two loaves of gluten free bread"></div>
  <div class="product-foot"><span class="price">£ 2.50</span><span class="add">Add to</span>
    <svg class="corner" width="34" height="34" viewBox="0 0 34 34"><path d="M34 0V34H0Z" fill="var(--green)"/><path d="M24 22v8M20 26h8" stroke="#fff" stroke-width="1.6"/></svg></div>
</article>

<footer class="site-footer abs">
  <div class="footer-band abs"></div>
  <div class="footer-col abs" style="left:106px">
    <h4>Useful links</h4>
    <ul class="link-list" style="margin-left:-8px">
      <li>Contact us</li><li>FAQs</li><li>Site Map</li><li>Privacy Policy</li>
    </ul>
  </div>
  <div class="footer-col newsletter abs" style="left:351px">
    <h4>Newsletter sign up</h4>
    <p>To keep upto date with the latest news and information about our services please fill out your Email address below:</p>
    <div class="news-field"><span></span><b><svg width="18" height="18" viewBox="0 0 18 18"><circle cx="9" cy="9" r="7.5" fill="none" stroke="#fff" stroke-width="1.4"/><path d="M5 9h7M9 6l3 3-3 3" fill="none" stroke="#fff" stroke-width="1.4"/></svg></b></div>
  </div>
  <div class="footer-col abs" style="left:605px">
    <h4>Your account</h4>
    <ul class="link-list" style="margin-left:-4px">
      <li>Create Account</li><li>Sign In</li><li>Shopping basket</li><li>Store Locations</li><li>Customer Service</li>
    </ul>
  </div>
  <div class="footer-col contact abs" style="left:850px">
    <h4>Stay in touch</h4>
    <p>27 Millrace Lane,<br>Elmbury,<br>Northshire , EB4 2QT</p>
    <p style="margin-top:2px">+44(0) 1632 960 418</p>
    <p class="mail">hello@wheatlesstable.example</p>
    <div class="social"><span style="background:#2aa3df"></span><span style="background:#3b5a9a"></span><span style="background:#d24234"></span><span style="background:#c8232c"></span></div>
  </div>
  <div class="copyright abs">Copyright © 2013 Foldline Studio. Use of this website constitutes acceptance of our User Agreement and Privacy Policy.</div>
</footer>

</body>
</html>
```